New website

We ned to create a new website that reflects more who we are. We are delivering exclusive premium products to our customers and the current website does not reflect our products at all.
We believe in less is more and need a webpage that is clean yet professional and exclusive.

Target Market(s)

Dentistry

Industry/Entity Type

Dental

Number of Pages Required

5+ page

Font styles to use
Sans Serif

Colors

Designer to choose colors to be used in the design.

Requirements
Must have
• Picture gallery
• Nice structure
• Clean layout
Nice to have
• Light fonts
Should not have
• Any italic font styles

```html
<!DOCTYPE html>
<html lang="en">
<head>
<meta charset="utf-8">
<title>Brightora</title>
<link rel="stylesheet" href="https://fonts.googleapis.com/css2?family=Montserrat:wght@400;500;600;700&family=Open+Sans:wght@400;600;700&display=swap">
<style>
:root{
  --ink:#222;
  --topbar:#3a3a3a;
  --footer:#2e2e2e;
  --nav:#0b5ea8;
  --blue:#2f7bbf;
  --blue-light:#5d9bd3;
  --blue-mid:#3f86c8;
  --heading:#1d5c9c;
  --red:#e0213c;
  --brand-ink:#333;
  --white:#fff;
}
*{box-sizing:border-box;margin:0;padding:0}
html,body{width:1200px;height:3422px;overflow:hidden;background:var(--white)}
body{position:relative;font-family:"Open Sans",Arial,sans-serif;color:var(--ink)}
.abs{position:absolute}
.btn{position:absolute;display:flex;align-items:center;justify-content:center;background:var(--red);color:var(--white);font:600 14px "Montserrat",Arial,sans-serif;border-radius:6px}

.topbar{left:0;top:0;width:1200px;height:25px;background:var(--topbar);color:var(--white);font:600 13px "Open Sans",Arial,sans-serif}
.topbar .call{position:absolute;left:88px;top:4px}
.topbar .mail{position:absolute;left:552px;top:4px;display:flex;gap:8px;align-items:center}
.dots{display:flex;gap:8px}
.dots span{width:17px;height:17px;border-radius:50%;background:var(--white);display:block}
.topbar .dots{position:absolute;left:955px;top:4px}

.header{left:0;top:25px;width:1200px;height:123px}
.brand{position:absolute;left:0;right:0;top:40px;display:flex;align-items:center;justify-content:center;gap:12px}
.brand .dot{width:26px;height:26px;border-radius:50%;background:var(--nav)}
.brand .name{font:500 32px "Montserrat",Arial,sans-serif;color:var(--brand-ink)}

.nav{left:0;top:148px;width:1200px;height:60px;background:var(--nav);display:flex;justify-content:center;align-items:center}
.nav a{color:var(--white);text-decoration:none;font:500 16px "Montserrat",Arial,sans-serif;padding:0 19px;border-right:1px solid rgba(255,255,255,.45);line-height:26px}
.nav a:last-of-type{border-right:none}
.nav svg{margin-left:20px}

.hero{left:0;top:208px;width:1200px;height:495px;background:linear-gradient(180deg,#bfe2f1 0%,#d9ecf4 55%,#b8b3dd 100%)}
.hero-photo{position:absolute;right:0;top:0;width:620px;height:495px;background:radial-gradient(ellipse at 55% 45%,#e9c3ae 0%,#d6a58c 35%,rgba(183,180,222,0) 75%)}
.hero h1{position:absolute;left:114px;top:160px;font:500 40px "Montserrat",Arial,sans-serif;color:var(--red)}
.hero p{position:absolute;left:84px;top:215px;width:460px;text-align:center;font:600 12.5px/18px "Open Sans",Arial,sans-serif;color:#444}
.hero .btn{left:255px;top:270px;width:158px;height:39px;background:var(--nav)}

.features{left:98px;top:661px;width:1008px;height:297px;display:flex}
.feature{flex:1;color:var(--white);text-align:center;padding-top:68px;background:var(--blue-light)}
.feature:nth-child(2){background:var(--blue-mid)}
.feature h3{font:500 19px "Montserrat",Arial,sans-serif;margin:18px 0 10px}
.feature p{font:700 12.5px/17px "Open Sans",Arial,sans-serif;padding:0 52px}
.feature .more{display:inline-flex;gap:6px;align-items:center;margin-top:20px;font:600 13px "Open Sans",Arial,sans-serif}

.welcome{left:0;top:1010px;width:1200px;text-align:center}
.welcome h2{font:600 25px "Montserrat",Arial,sans-serif;color:var(--heading)}
.rule{width:50px;height:2px;background:var(--red);margin:6px auto 0}
.welcome p{font:400 13.5px/19px "Open Sans",Arial,sans-serif;width:1060px;margin:12px auto 0}
.welcome .btn{left:515px;top:240px;width:156px;height:34px}

.gallery{left:0;top:1323px;width:1200px;height:538px;background:var(--blue)}
.gallery h2{position:absolute;left:0;right:0;top:30px;text-align:center;color:var(--white);font:600 27px "Montserrat",Arial,sans-serif}
.card{position:absolute;top:105px;width:236px}
.card .photo{height:210px;background:linear-gradient(180deg,#c9877c 0%,#ece3da 50%,#b96b63 100%);position:relative}
.card .label{position:absolute;left:0;right:0;bottom:0;height:40px;background:rgba(214,50,66,.88);color:var(--white);font:600 26px "Montserrat",Arial,sans-serif;display:flex;align-items:center;justify-content:center}
.card p{color:var(--white);font:600 12px/17px "Open Sans",Arial,sans-serif;text-align:center;margin-top:20px;padding:0 14px}
.card .btn{position:relative;width:110px;height:24px;margin:10px auto 0;font-size:11px;border-radius:3px}
.arrow{position:absolute;top:207px;width:32px;height:32px}

.services h2,.smile h2{font:600 27px "Montserrat",Arial,sans-serif;color:var(--heading)}
.services{left:137px;top:1910px;width:451px;text-align:center}
.services h2{text-align:right}
.services .rule{margin:6px 0 0 auto;width:58px}
.services p{font:400 13.5px/19px "Open Sans",Arial,sans-serif;margin-top:22px}
.services .btn{left:292px;top:308px;width:158px;height:39px}
.services-photo{left:641px;top:1909px;width:481px;height:331px;background:linear-gradient(135deg,#b8d9ec 0%,#e8c8b6 50%,#7fb2d4 100%)}

.smile-photo{left:132px;top:2329px;width:450px;height:331px;background:linear-gradient(135deg,#6b5446 0%,#d7ab92 50%,#8a6a58 100%)}
.smile{left:634px;top:2320px;width:480px}
.smile .rule{margin:6px 0 0 0;width:58px}
.smile p{font:400 13.5px/19px "Open Sans",Arial,sans-serif;margin-top:14px}
.smile .btn{left:2px;top:303px;width:156px;height:37px}

.map{left:0;top:2714px;width:1200px;height:370px;background:linear-gradient(120deg,#e8eedf 0%,#e5e8dc 45%,#a9c9f1 50%,#e4e8db 60%,#a9c9f1 100%)}

.contact{left:0;top:3084px;width:1200px;height:283px;background:#2a78bb;color:var(--white);text-align:center}
.contact h2{margin-top:54px;font:600 20px "Montserrat",Arial,sans-serif}
.contact .sub{font:400 16px/20px "Open Sans",Arial,sans-serif;width:470px;margin:6px auto 0}
.info{position:absolute;top:146px;width:300px;text-align:center;font:700 14px "Open Sans",Arial,sans-serif}
.info svg{display:block;margin:0 auto 18px}

.footer{left:0;top:3367px;width:1200px;height:55px;background:var(--footer);color:var(--white)}
.footer .copy{position:absolute;left:108px;top:18px;font:600 15px "Open Sans",Arial,sans-serif}
.footer .dots{position:absolute;left:930px;top:18px}
</style>
</head>
<body>

<div class="abs topbar">
  <div class="call">Call Today : 123-555-0147</div>
  <div class="mail">
    <svg width="16" height="12" viewBox="0 0 16 12"><rect x="0.5" y="0.5" width="15" height="11" fill="#fff"/><path d="M1 1l7 6 7-6" stroke="#3a3a3a" fill="none"/></svg>
    hello@brightora.com
  </div>
  <div class="dots"><span></span><span></span><span></span><span></span><span></span></div>
</div>

<header class="abs header">
  <div class="brand"><div class="dot"></div><div class="name">Brightora</div></div>
</header>

<nav class="abs nav">
  <a>WELCOME</a><a>PRODUCTS</a><a>SPECIAL SERVICES</a><a>SMILE GALLERY</a><a>SHADE ANALYSIS</a><a>CONTACT</a>
  <svg width="18" height="18" viewBox="0 0 18 18"><circle cx="7" cy="7" r="5.5" stroke="#fff" stroke-width="2.5" fill="none"/><path d="M11 11l5.5 5.5" stroke="#fff" stroke-width="2.5"/></svg>
</nav>

<section class="abs hero">
  <div class="hero-photo" role="img" aria-label="Smiling woman with long hair against a bright sky"></div>
  <h1>Brightora &amp; function</h1>
  <p>Lorem Ipsum is simply dummy text of the printing and industry.<br>Lorem Ipsum has been the industry's</p>
  <div class="btn">Read More..</div>
</section>

<section class="abs features">
  <div class="feature">
    <svg width="60" height="60" viewBox="0 0 60 60" fill="none" stroke="#fff" stroke-width="2.5"><path d="M14 12c6-4 10 0 16 0s10-4 16 0 4 16 0 22c-2 8-3 18-7 18-4 0-4-14-9-14s-5 14-9 14c-4 0-5-10-7-18-4-6-6-18 0-22z"/><path d="M50 4v8M46 8h8"/></svg>
    <h3>PRODUCT</h3>
    <p>Lorem Ipsum is simply dummy text of the printing and industry. Lorem Ipsum industry's</p>
    <div class="more">Read More.. <svg width="16" height="16" viewBox="0 0 16 16"><circle cx="8" cy="8" r="7" stroke="#fff" fill="none" stroke-width="1.5"/><path d="M5 8h6M8 5l3 3-3 3" stroke="#fff" fill="none" stroke-width="1.5"/></svg></div>
  </div>
  <div class="feature">
    <svg width="60" height="60" viewBox="0 0 60 60" fill="none" stroke="#fff" stroke-width="2.5"><circle cx="28" cy="12" r="6"/><path d="M10 30l12 10h20l8 12M22 40l-6 14M30 22l6 16"/><path d="M44 20l8-6"/></svg>
    <h3>SPECIAL SERVICES</h3>
    <p>Lorem Ipsum is simply dummy text of the printing and industry. Lorem Ipsum industry's</p>
    <div class="more">Read More.. <svg width="16" height="16" viewBox="0 0 16 16"><circle cx="8" cy="8" r="7" stroke="#fff" fill="none" stroke-width="1.5"/><path d="M5 8h6M8 5l3 3-3 3" stroke="#fff" fill="none" stroke-width="1.5"/></svg></div>
  </div>
  <div class="feature">
    <svg width="60" height="60" viewBox="0 0 60 60" fill="none" stroke="#fff" stroke-width="2.5"><circle cx="30" cy="30" r="26"/><circle cx="21" cy="24" r="2" fill="#fff"/><circle cx="39" cy="24" r="2" fill="#fff"/><path d="M18 36c6 8 18 8 24 0"/></svg>
    <h3>SMILE GALLERY</h3>
    <p>Lorem Ipsum is simply dummy text of the printing and industry. Lorem Ipsum industry's</p>
    <div class="more">Read More.. <svg width="16" height="16" viewBox="0 0 16 16"><circle cx="8" cy="8" r="7" stroke="#fff" fill="none" stroke-width="1.5"/><path d="M5 8h6M8 5l3 3-3 3" stroke="#fff" fill="none" stroke-width="1.5"/></svg></div>
  </div>
</section>

<section class="abs welcome">
  <h2>Welcome to Brightora</h2>
  <div class="rule"></div>
  <p>Who designed this Smile?</p>
  <p>Brightora smiles has a very distinctive appearance and character. Both these Brightora features owe as much to their owners as to our dental artisans, because in the final analysis, people who buy a new smile also designs them.</p>
  <p>Inevitably, the greater the demands a smile has to meet, the lower the lowest denominator.</p>
  <p>That´s why standard production line smiles have such little character. With our highstrength ceramics our aim has never been to create less expensive smiles for the majority, but the perfect smile for few.Isn´t it time you joined the few?</p>
  <div class="btn">Read More..</div>
</section>

<section class="abs gallery">
  <h2>Product Gallery</h2>
  <div class="rule" style="position:absolute;left:575px;top:76px;margin:0"></div>
  <svg class="arrow" style="left:48px" viewBox="0 0 32 32"><circle cx="16" cy="16" r="14" fill="none" stroke="#fff" stroke-width="2"/><path d="M19 9l-7 7 7 7" fill="none" stroke="#fff" stroke-width="3"/></svg>
  <svg class="arrow" style="left:1130px" viewBox="0 0 32 32"><circle cx="16" cy="16" r="14" fill="none" stroke="#fff" stroke-width="2"/><path d="M13 9l7 7-7 7" fill="none" stroke="#fff" stroke-width="3"/></svg>
  <div class="card" style="left:103px"><div class="photo" role="img" aria-label="Close-up of teeth with veneers"><div class="label">Veneers</div></div><p>Lorem Ipsum is simply dummy printing and typesetting industry. ever since the 1500s,</p><div class="btn">Read More..</div></div>
  <div class="card" style="left:356px"><div class="photo" role="img" aria-label="Close-up of teeth with pressed ceramic restorations"><div class="label">Press Ceramic</div></div><p>Lorem Ipsum is simply dummy printing and typesetting industry. ever since the 1500s,</p><div class="btn">Read More..</div></div>
  <div class="card" style="left:607px"><div class="photo" role="img" aria-label="Close-up of front teeth with resin crowns" style="background:linear-gradient(180deg,#f1e9e4 0%,#ffffff 50%,#c7a89d 100%)"><div class="label">Resin Crowns</div></div><p>Lorem Ipsum is simply dummy printing and typesetting industry. ever since the 1500s,</p><div class="btn">Read More..</div></div>
  <div class="card" style="left:860px"><div class="photo" role="img" aria-label="Dental implant bridge on gums" style="background:linear-gradient(180deg,#d7a6a8 0%,#efe6dc 55%,#c4848b 100%)"><div class="label">Implants</div></div><p>Lorem Ipsum is simply dummy printing and typesetting industry. ever since the 1500s,</p><div class="btn">Read More..</div></div>
</section>

<section class="abs services">
  <h2>Special Services</h2>
  <div class="rule"></div>
  <p>Brightora ensures exact teeth reconstruction, individual service of the customer and technical information. We can also offer our customers additional service on favorable terms.The below specified additional services are only a part of what we can offer to you andyour patients</p>
  <p style="margin-top:16px">Brightora Cosmetic Imaging is the first step in creating a blueprint for success. The patient can see the final result before taking any decisions.<br>Click the links in the menu above to learn more!</p>
  <div class="btn">Read More..</div>
</section>
<div class="abs services-photo" role="img" aria-label="Patient in a dental chair during a check-up"></div>

<div class="abs smile-photo" role="img" aria-label="Portrait of a smiling young woman"></div>
<section class="abs smile">
  <h2>Smile Gallery</h2>
  <div class="rule"></div>
  <p style="margin-top:22px">This patient had problems with seveere crooked teeth that made the smile unaesthetic. Brightora provided 6 fullceramic veneers to restore the beauty of a natural smile.</p>
  <p>This patient had problems with a gummy smile and minor diastemas between her teeth. To creat a natural looking smile Brightora provided 4 fullceramic veneers.</p>
  <p>This patient had problems with crooked teeth that made the smile unnatural and unaesthetic. Brightora provided 8 fullceramic veneers to restore the beauty of a natural apperance and a straight smile.</p>
  <p>Click the links in the menu above to learn more!</p>
  <div class="btn">Read More..</div>
</section>

<div class="abs map" role="img" aria-label="Road map of the region around the clinic"></div>

<section class="abs contact">
  <h2>GET IN TOUCH WITH US</h2>
  <p class="sub">Lorem ipsum dolor sit amet consectetur adipiscing elit sed do eiusmod tempor.</p>
  <div class="info" style="left:62px">
    <svg width="42" height="42" viewBox="0 0 42 42" fill="none" stroke="#fff" stroke-width="2"><circle cx="21" cy="21" r="19"/><path d="M21 31s-7-8-7-13a7 7 0 0114 0c0 5-7 13-7 13z"/><circle cx="21" cy="18" r="2.5"/></svg>
    Lindgatan 14B 211 40 Malmö.
  </div>
  <div class="info" style="left:466px">
    <svg width="42" height="42" viewBox="0 0 42 42" fill="none" stroke="#fff" stroke-width="2"><circle cx="21" cy="21" r="19"/><path d="M15 12l4 0 2 5-3 2c1 3 3 5 6 6l2-3 5 2v4c-8 1-17-8-16-16z"/></svg>
    +46-40-12 34 50
  </div>
  <div class="info" style="left:774px">
    <svg width="42" height="42" viewBox="0 0 42 42" fill="none" stroke="#fff" stroke-width="2"><circle cx="21" cy="21" r="19"/><rect x="12" y="15" width="18" height="12"/><path d="M12 15l9 7 9-7"/></svg>
    hello@brightora.com
  </div>
</section>

<footer class="abs footer">
  <div class="copy">© 2017 Brightora - All Rights Reserved</div>
  <div class="dots"><span></span><span></span><span></span><span></span><span></span></div>
</footer>

</body>
</html>
```